SOS! The Bramble cafe is in need of a menu face lift!

We need a standout looking menu for our evolving cafe. Our business has grown greatly from our fresh and changing menu, however the menu (look) itself isn't inspiring and is basic.
I have attached some photos of the business and menus I like the look of.
I am open to other ideas (this is why I need your creative help)
Our menu is currently on an A5 clip board, however we are willing to change it a different size if needed.
Updates

Would love to have it a multi function eg, used as a takeaway menu as well, possibly bi-fold? Added Wednesday, June 8, 2016

Industry/Entity Type

Business

Requirements
Nice to have
• It would be cool to have some old sea/ pirate references?

```html
<!DOCTYPE html>
<html lang="en">
<head>
<meta charset="utf-8">
<title>The Bramble – Menu</title>
<link rel="stylesheet" href="https://fonts.googleapis.com/css2?family=Oswald:wght@300;500;700&family=Special+Elite&family=Courier+Prime:wght@400;700&display=swap">
<style>
  :root {
    --backdrop: #ecebe6;
    --paper: #dddbcc;
    --paper-edge: #c9c6b4;
    --ink: #242424;
    --ink-soft: #4a4a46;
    --band: #b9b7aa;
    --accent-blue: #4f6d86;
  }
  * { box-sizing: border-box; margin: 0; padding: 0; }
  html, body { width: 1200px; height: 1200px; overflow: hidden; background: var(--backdrop); }
  body { position: relative; font-family: "Courier Prime", monospace; color: var(--ink); }

  .menu-sheet {
    position: absolute; left: 40px; top: 80px; width: 760px; height: 1040px;
    background: var(--paper); display: grid;
    grid-template-columns: 1fr 1fr; grid-template-rows: 1fr 1fr;
    box-shadow: 0 2px 10px rgba(0,0,0,.15);
  }
  .panel { padding: 22px 24px; position: relative; }
  .panel--tl, .panel--bl { border-right: 2px dashed var(--ink); }
  .panel--tl, .panel--tr { border-bottom: 2px dashed var(--ink); }

  .panel-head {
    display: flex; align-items: stretch; gap: 10px; margin-bottom: 14px;
  }
  .panel-title { font-family: "Oswald", sans-serif; font-weight: 700; font-size: 30px; text-transform: uppercase; letter-spacing: .5px; line-height: 1; padding: 6px 0; white-space: nowrap; }
  .panel-band {
    flex: 1; background: var(--band);
    display: flex; align-items: flex-end; justify-content: flex-end; padding: 4px 6px;
  }
  .panel-note { font-family: "Oswald", sans-serif; font-weight: 500; font-size: 11px; text-transform: uppercase; text-align: right; line-height: 1.2; }

  .section-title { font-family: "Oswald", sans-serif; font-weight: 700; font-size: 18px; text-transform: uppercase; margin: 4px 0 2px; }
  .section-sub { font-size: 9.5px; color: var(--ink-soft); margin-bottom: 8px; border-bottom: 1px dashed var(--ink); padding-bottom: 6px; }

  .item { margin-bottom: 9px; }
  .item-row { display: flex; justify-content: space-between; align-items: baseline; gap: 8px; }
  .item-name { font-family: "Special Elite", monospace; font-size: 13.5px; text-transform: uppercase; }
  .item-price { font-family: "Special Elite", monospace; font-size: 13px; white-space: nowrap; }
  .item-desc { font-size: 9.5px; color: var(--ink-soft); line-height: 1.25; margin-top: 1px; }

  .sides-list { list-style: none; font-family: "Special Elite", monospace; font-size: 12.5px; }
  .sides-list li { display: flex; justify-content: space-between; padding: 3px 0; border-bottom: 1px dotted var(--paper-edge); }

  .brand-mark { display: flex; align-items: center; gap: 8px; margin-top: 18px; }
  .brand-dot { width: 22px; height: 22px; border-radius: 50%; background: var(--accent-blue); }
  .brand-name { font-family: "Oswald", sans-serif; font-weight: 500; font-size: 16px; text-transform: uppercase; letter-spacing: 1px; }

  .footnote { font-size: 9.5px; color: var(--ink-soft); margin-top: 12px; line-height: 1.3; }

  .cover {
    position: absolute; left: 830px; top: 340px; width: 330px; height: 500px;
    background: var(--paper); box-shadow: 0 2px 10px rgba(0,0,0,.15);
    border-left: 2px dashed var(--ink); border-right: 2px dashed var(--ink);
    display: flex; flex-direction: column; align-items: center; justify-content: center; gap: 14px;
  }
  .cover-dot { width: 46px; height: 46px; border-radius: 50%; background: var(--accent-blue); }
  .cover-name { font-family: "Oswald", sans-serif; font-weight: 300; font-size: 34px; text-transform: uppercase; letter-spacing: 2px; }
  .cover-tag { font-family: "Oswald", sans-serif; font-weight: 300; font-size: 13px; text-transform: uppercase; letter-spacing: 3px; color: var(--ink-soft); }
</style>
</head>
<body>
  <main class="menu-sheet">
    <section class="panel panel--tl">
      <header class="panel-head"><h2 class="panel-title">Breakfast Menu</h2><div class="panel-band"><span class="panel-note">All day</span></div></header>
      <div class="item"><div class="item-row"><span class="item-name">2 Slices Toast</span><span class="item-price">$4.5</span></div><p class="item-desc">White or wholemeal, jam, yeast spread, honey, peanut butter or cinnamon sugar</p></div>
      <div class="item"><div class="item-row"><span class="item-name">GF Bread (2)</span><span class="item-price">+$0.5</span></div></div>
      <div class="item"><div class="item-row"><span class="item-name">Turkish Raisin (2) Toast</span><span class="item-price">$5.5</span></div></div>
      <div class="item"><div class="item-row"><span class="item-name">Banana Bread (GF)</span><span class="item-price">$5.5</span></div><p class="item-desc">Served with whipped butter</p></div>
      <div class="item"><div class="item-row"><span class="item-name">Granola &amp; Muesli</span><span class="item-price">$5.5</span></div><p class="item-desc">House made with yoghurt &amp; berry compote</p></div>
      <div class="item"><div class="item-row"><span class="item-name">Spanish Eggs</span><span class="item-price">$12.5</span></div><p class="item-desc">Two poached eggs in tomato salsa with feta &amp; sourdough</p></div>
      <div class="item"><div class="item-row"><span class="item-name">Bacon &amp; Eggs</span><span class="item-price">$12.5 / $14.5</span></div></div>
      <div class="item"><div class="item-row"><span class="item-name">Bacon &amp; Egg Sandwich</span><span class="item-price">$10</span></div></div>
      <div class="item"><div class="item-row"><span class="item-name">Lifestyle Breakfast</span><span class="item-price">$17.5</span></div><p class="item-desc">Poached eggs, spinach, tomato, avocado &amp; toast</p></div>
      <div class="item"><div class="item-row"><span class="item-name">Eggs Benedict</span><span class="item-price">$17.5</span></div></div>
      <div class="item"><div class="item-row"><span class="item-name">The Big Bramble Breakfast</span><span class="item-price">$19.5</span></div></div>
      <div class="item"><div class="item-row"><span class="item-name">French Toast</span><span class="item-price">$15.5</span></div></div>
      <div class="item"><div class="item-row"><span class="item-name">Pancakes – two stack</span><span class="item-price">$15.5</span></div></div>
    </section>

    <section class="panel panel--tr">
      <header class="panel-head"><h2 class="panel-title">Lunch Menu</h2><div class="panel-band"><span class="panel-note">Mon to Fri 2:30pm<br>Sat &amp; Sun 1:30pm</span></div></header>
      <h3 class="section-title">Wraps</h3>
      <p class="section-sub">Lightly toasted &amp; served with beer battered chips</p>
      <div class="item"><div class="item-row"><span class="item-name">Chicken</span><span class="item-price">$15.5</span></div><p class="item-desc">Bacon, lettuce, cheese &amp; your choice of sauce</p></div>
      <div class="item"><div class="item-row"><span class="item-name">Bramble</span><span class="item-price">$16.5</span></div><p class="item-desc">Crumbed chicken, tomato, feta &amp; aioli</p></div>
      <div class="item"><div class="item-row"><span class="item-name">Vegie Wrap</span><span class="item-price">$15.5</span></div><p class="item-desc">Grilled mushroom, capsicum, spinach &amp; balsamic</p></div>
      <div class="item"><div class="item-row"><span class="item-name">Lentil Wrap</span><span class="item-price">$15.5</span></div><p class="item-desc">Own lentil patty, lettuce, tomato &amp; chutney</p></div>
      <div class="item"><div class="item-row"><span class="item-name">Chicken Fajita</span><span class="item-price">$15.5</span></div><p class="item-desc">Seasoned chicken, capsicum, onion &amp; sour cream</p></div>
      <div class="item"><div class="item-row"><span class="item-name">Beef Burrito</span><span class="item-price">$16.5</span></div><p class="item-desc">Seasoned beef, rice, black beans &amp; salsa</p></div>
    </section>

    <section class="panel panel--bl">
      <h3 class="section-title">Sides &amp; Extras</h3>
      <p class="section-sub">Add to any meal</p>
      <ul class="sides-list">
        <li><span>Croissant</span><span>$5</span></li>
        <li><span>Extra egg</span><span>$3</span></li>
        <li><span>Bacon</span><span>$4</span></li>
        <li><span>Hash brown</span><span>$3</span></li>
        <li><span>Avocado</span><span>$4</span></li>
        <li><span>Chips / wedges</span><span>$6</span></li>
      </ul>
      <p class="footnote">Please ask our friendly crew about dietary needs. Gluten free bread available.</p>
      <div class="brand-mark"><span class="brand-dot"></span><span class="brand-name">The Bramble</span></div>
    </section>

    <section class="panel panel--br">
      <h3 class="section-title">House Made Chicken Schnitzels</h3>
      <p class="section-sub">All served with chips &amp; salad</p>
      <div class="item"><div class="item-row"><span class="item-name">Housemade Schnitzel</span><span class="item-price">$19.5</span></div><p class="item-desc">Mushroom, pepper or plain gravy</p></div>
      <div class="item"><div class="item-row"><span class="item-name">Chicken &amp; Avocado</span><span class="item-price">$22.5</span></div></div>
      <div class="item"><div class="item-row"><span class="item-name">Parma</span><span class="item-price">$22.5</span></div><p class="item-desc">Topped with tomato sauce, ham &amp; cheese</p></div>
      <div class="item"><div class="item-row"><span class="item-name">Hawaiian</span><span class="item-price">$23.5</span></div></div>
      <h3 class="section-title">Burgers</h3>
      <p class="section-sub">Served with beer battered chips</p>
      <div class="item"><div class="item-row"><span class="item-name">B.L.T.</span><span class="item-price">$14.5</span></div></div>
      <div class="item"><div class="item-row"><span class="item-name">Lentil Burger</span><span class="item-price">$15.5</span></div></div>
      <div class="item"><div class="item-row"><span class="item-name">Schnitzel Burger</span><span class="item-price">$16.5</span></div></div>
      <div class="item"><div class="item-row"><span class="item-name">Mexican Burger</span><span class="item-price">$16.5</span></div></div>
      <div class="item"><div class="item-row"><span class="item-name">Grilled Chicken Burger</span><span class="item-price">$16.5</span></div></div>
    </section>
  </main>

  <aside class="cover">
    <span class="cover-dot"></span>
    <h1 class="cover-name">The Bramble</h1>
    <p class="cover-tag">Coffee Bar &amp; Grill</p>
  </aside>
</body>
</html>
```